Interior design service, along with home organization, packing, and staging, home and business. As well as staging in conjunction with real estate sales.

Love many of your designs and will be choosing today. To inform you of the exact details needed, the name of the company is "Flourish by Marnie T" , my phone number and e-,ail need to be included. i also need either description or some sort of bullet points that give an idea of the following:

- Interior design for home and business
- Home organization and packing
- Staging for personal and professional space
- Real estate stagingĀ 

Thank you

Target Market(s)

wide audience, but most importantly people looking for a quality service

Industry/Entity Type

Real Estate

Contact Information for Business Card

Flourish By Marnie T
Marnie Toller
(555)617-3942
mtbriar@inboxly.example

Requirements
Must have
• I'm 29 so i want my card to reflect something professional but still fresh. I don't have any specific photos or quotes that Ive included, however I like the card to reflect a personal touch, which is what I'm seeking from this service in the design of my card. Thanks!

```html
<!DOCTYPE html>
<html lang="en">
<head>
<meta charset="utf-8">
<title>Flourish By Marnie T – Business Card</title>
<link rel="stylesheet" href="https://fonts.googleapis.com/css2?family=Macondo&display=swap">
<style>
  :root {
    --stage: #2f2f2f;
    --card-taupe: #7b766d;
    --card-frame: #1c1a17;
    --ink-cream: #f2ecdc;
    --ink-dark: #1d1b18;
    --tone-orange: #e07a2b;
    --tone-green: #7e9a3a;
    --tone-teal: #8fbcb6;
    --tone-cream: #eae7bf;
    --tone-gold: #d9a45a;
  }
  * { box-sizing: border-box; margin: 0; padding: 0; }
  html, body {
    width: 1200px;
    height: 960px;
    overflow: hidden;
    background: var(--stage);
  }
  .canvas {
    position: relative;
    width: 1200px;
    height: 960px;
    font-family: "Macondo", cursive;
  }
  .card {
    position: absolute;
    background: var(--card-taupe);
    overflow: hidden;
  }
  .card--front { left: 174px; top: 68px; width: 576px; height: 336px; }
  .card--back  { left: 444px; top: 462px; width: 566px; height: 332px; }
  .card__art {
    position: absolute;
    inset: 0;
    width: 100%;
    height: 100%;
  }
  .card__frame {
    position: absolute;
    inset: 11px;
    border: 1px solid var(--card-frame);
    pointer-events: none;
  }
  .services {
    position: absolute;
    right: 46px;
    top: 160px;
    list-style: none;
    font-size: 13px;
    line-height: 16px;
    color: var(--ink-cream);
    text-align: right;
  }
  .services__item::before { content: "• "; }
  .front__tagline {
    position: absolute;
    right: 46px;
    top: 232px;
    font-size: 18px;
    color: var(--ink-cream);
  }
  .front__name {
    position: absolute;
    right: 36px;
    top: 252px;
    font-size: 43px;
    font-weight: 400;
    line-height: 1;
    color: var(--ink-cream);
    white-space: nowrap;
  }
  .contact {
    position: absolute;
    left: 72px;
    top: 36px;
    display: grid;
    grid-template-columns: auto auto;
    column-gap: 16px;
    row-gap: 4px;
    font-size: 24px;
    line-height: 28px;
  }
  .contact__label { text-align: right; color: var(--ink-dark); }
  .contact__value { color: var(--ink-cream); white-space: nowrap; }
  .pitch {
    position: absolute;
    color: var(--ink-dark);
    white-space: nowrap;
    line-height: 1;
  }
  .pitch--lead { left: 174px; top: 148px; font-size: 28px; }
  .pitch--for  { left: 240px; top: 184px; font-size: 24px; }
  .pitch--main { left: 240px; top: 212px; font-size: 42px; }
</style>
</head>
<body>
<main class="canvas">

  <section class="card card--front" aria-label="Card front">
    <svg class="card__art" viewBox="0 0 576 336" role="img" aria-label="Abstract stained-glass mosaic of orange, green, teal and cream shards divided by white lines">
      <defs>
        <linearGradient id="mosaic-front" x1="0" y1="0" x2="1" y2="0.4">
          <stop offset="0" stop-color="var(--tone-cream)"/>
          <stop offset="0.35" stop-color="var(--tone-gold)"/>
          <stop offset="0.55" stop-color="var(--tone-orange)"/>
          <stop offset="0.75" stop-color="var(--tone-green)"/>
          <stop offset="1" stop-color="var(--tone-teal)"/>
        </linearGradient>
      </defs>
      <polygon points="0,0 576,0 576,48 0,258" fill="url(#mosaic-front)" opacity="0.85"/>
      <line x1="0" y1="262" x2="576" y2="52" stroke="var(--ink-cream)" stroke-width="4"/>
    </svg>
    <div class="card__frame"></div>
    <ul class="services">
      <li class="services__item">Interior design for home and business</li>
      <li class="services__item">Home organization and packing</li>
      <li class="services__item">Staging for personal and professional space</li>
      <li class="services__item">Real estate staging</li>
    </ul>
    <p class="front__tagline">Flourish By,</p>
    <h1 class="front__name">Marnie T</h1>
  </section>

  <section class="card card--back" aria-label="Card back">
    <svg class="card__art" viewBox="0 0 566 332" role="img" aria-label="Abstract stained-glass mosaic corner of orange, green, teal and cream shards">
      <defs>
        <linearGradient id="mosaic-back" x1="0" y1="0" x2="1" y2="1">
          <stop offset="0" stop-color="var(--tone-green)"/>
          <stop offset="0.4" stop-color="var(--tone-teal)"/>
          <stop offset="0.7" stop-color="var(--tone-orange)"/>
          <stop offset="1" stop-color="var(--tone-cream)"/>
        </linearGradient>
      </defs>
      <polygon points="0,104 310,332 0,332" fill="url(#mosaic-back)" opacity="0.85"/>
      <line x1="0" y1="100" x2="316" y2="334" stroke="var(--ink-cream)" stroke-width="4"/>
    </svg>
    <div class="card__frame"></div>
    <div class="contact">
      <span class="contact__label">Name</span><span class="contact__value">Marnie Toller</span>
      <span class="contact__label">Phone</span><span class="contact__value">(555)617-3942</span>
      <span class="contact__label">Email</span><span class="contact__value">mtbriar@inboxly.example</span>
    </div>
    <p class="pitch pitch--lead">Are you looking</p>
    <p class="pitch pitch--for">for</p>
    <p class="pitch pitch--main">quality service?</p>
  </section>

</main>
</body>
</html>
```